Lanterns Under Glass (CD cover)

A CD cover that incorporates (if possible) a photo (or photos) with original art. (I'm flexible on this) Should have a sense of mystery... pensive, but also suggest expansiveness.

I'm open to putting photo on front of CD and art on back or inside, or vice versa, as I don't think they can be incorporated effectively??

I need a design primarily for the front, but possibly the back too (in other words, the sections that will be most visible prior to opening the CD.) This will be a "sleeve" or wallet style CD cover with 4 panels.

I'm including the liner notes, list of songs, artists, etc, but it's not necessary to lay that out too as that will be in the inside panels.

Target Market(s)

Jazz and independent/original music listeners

Industry/Entity Type

Artists

Requirements
Must have
• Cover:
Title of CD
My name
Names of band members
Photo or Art

Back or Inside:
Song titles
Photos of band and recording session
Introductory/explanatory verbiage
Nice to have
• Original art
Should not have
• No need to incorporate the liner notes attached - this was provided simply to give more information to designers - to give them more of a feel of what the album is about.

```html
<!DOCTYPE html>
<html lang="en">
<head>
<meta charset="utf-8">
<title>Lanterns Under Glass – Back Traycard</title>
<link rel="stylesheet" href="https://fonts.googleapis.com/css2?family=Cormorant+Garamond:ital,wght@1,500&family=Oswald:wght@500&family=Roboto:wght@400&family=Roboto+Condensed:ital,wght@0,300;0,400;1,300;1,700&display=swap">
<style>
  :root{
    --paper:#ffffff;
    --ochre-dark:#c9961c;
    --ochre:#e2b320;
    --yellow:#f7d81f;
    --yellow-pale:#fbe97a;
    --cream:#fdf3c0;
    --earth:#6b4a14;
    --earth-deep:#3a250a;
    --ink:#4a3206;
    --ink-soft:#5b4010;
    --numeral:rgba(120,100,70,.55);
    --ghost:rgba(255,244,190,.16);
    --photo-dark:#141210;
    --label:#222222;
  }
  *{margin:0;padding:0;box-sizing:border-box}
  html,body{width:1200px;height:1181px;overflow:hidden;background:var(--paper)}
  .sheet{position:relative;width:1200px;height:1181px;background:var(--paper)}
  .traycard{
    position:absolute;left:48px;top:64px;width:1105px;height:950px;overflow:hidden;
    background:
      linear-gradient(180deg, transparent 0 88%, rgba(107,74,20,.6) 91%, var(--earth-deep) 95%, var(--earth) 100%),
      radial-gradient(ellipse 55% 35% at 55% 62%, var(--cream) 0%, rgba(253,243,192,0) 70%),
      linear-gradient(180deg, var(--ochre-dark) 0%, var(--ochre) 20%, var(--yellow) 45%, var(--yellow-pale) 68%, var(--ochre) 86%);
  }
  .ghost-name{
    position:absolute;font-family:"Oswald",sans-serif;font-weight:500;color:var(--ghost);
    letter-spacing:-2px;line-height:1;white-space:nowrap;
  }
  .ghost-name.first{left:-10px;top:-40px;font-size:300px}
  .ghost-name.last{left:-20px;top:320px;font-size:300px}
  .tracklist{position:absolute;left:0;top:46px;list-style:none}
  .track{position:relative;height:68px;padding-left:105px}
  .track-no{
    position:absolute;right:calc(100% - 100px);top:-8px;font-family:"Cormorant Garamond",serif;
    font-style:italic;font-weight:500;font-size:58px;line-height:1;color:var(--numeral);
  }
  .track-title{font-family:"Roboto Condensed",sans-serif;font-weight:300;font-size:20px;line-height:26px;color:var(--ink)}
  .track-credit{font-family:"Roboto Condensed",sans-serif;font-style:italic;font-weight:700;font-size:17.5px;line-height:26px;color:var(--ink-soft)}
  .portrait{
    position:absolute;left:648px;top:49px;width:414px;height:501px;
    background:radial-gradient(ellipse 60% 55% at 55% 50%, #3b2a20 0%, #201813 55%, var(--photo-dark) 100%);
  }
  .personnel{
    position:absolute;left:630px;top:599px;width:450px;text-align:center;
    font-family:"Roboto Condensed",sans-serif;font-style:italic;font-weight:700;font-size:17.5px;line-height:26px;color:var(--ink-soft)
  }
  .personnel .guests{margin-top:26px}
  .production{
    position:absolute;left:0;top:860px;width:1105px;text-align:center;
    font-family:"Roboto Condensed",sans-serif;font-style:italic;font-weight:700;font-size:15px;line-height:24px;color:var(--cream)
  }
  .panel-label{
    position:absolute;left:0;top:1087px;width:1200px;text-align:center;
    font-family:"Roboto",sans-serif;font-weight:400;font-size:22px;color:var(--label);letter-spacing:-.2px
  }
</style>
</head>
<body>
<div class="sheet">
  <section class="traycard">
    <div class="ghost-name first" aria-hidden="true">MARA</div>
    <div class="ghost-name last" aria-hidden="true">VELLIN</div>

    <ol class="tracklist">
      <li class="track"><span class="track-no">1</span><p class="track-title">Hold On, We're Here For You</p><p class="track-credit">Mara Vellin; Arranged by Gus Tremaine</p></li>
      <li class="track"><span class="track-no">2</span><p class="track-title">Amber Season</p><p class="track-credit">Harlan Pike – music, June Pike – lyrics;<br>Arranged by Dorian Calloway</p></li>
      <li class="track" style="margin-top:26px"><span class="track-no">3</span><p class="track-title">Lanterns Under Glass</p><p class="track-credit">Gus Tremaine; Arranged by Gus Tremaine</p></li>
      <li class="track"><span class="track-no">4</span><p class="track-title">Only This, Only Now</p><p class="track-credit">Mara Vellin; Arranged by Gus Tremaine</p></li>
      <li class="track"><span class="track-no">5</span><p class="track-title">Carnival*</p><p class="track-credit">Benny Marlowe; Arranged by Gus Tremaine</p></li>
      <li class="track"><span class="track-no">6</span><p class="track-title">Hushed</p><p class="track-credit">Mara Vellin; Arranged by Gus Tremaine</p></li>
      <li class="track"><span class="track-no">7</span><p class="track-title">So Kind</p><p class="track-credit">Gus Tremaine; Arranged by Gus Tremaine</p></li>
      <li class="track"><span class="track-no">8</span><p class="track-title">Keep the Little One**</p><p class="track-credit">Arnold Hale Jr &amp; Bessie Harlow; Arranged by Mara Vellin</p></li>
      <li class="track"><span class="track-no">9</span><p class="track-title">The Simple Sight of You</p><p class="track-credit">Roy Nolan; Arranged by Gus Tremaine &amp; Mara Vellin</p></li>
      <li class="track"><span class="track-no">10</span><p class="track-title">Overture to a Sigh</p><p class="track-credit">Dale Ellory; Arranged by Dorian Calloway</p></li>
      <li class="track"><span class="track-no">11</span><p class="track-title">Finer Than Everything</p><p class="track-credit">Daniel Lockwood; Dean Wheaton;<br>Arranged by Gus Tremaine &amp; Mara Vellin</p></li>
    </ol>

    <div class="portrait" role="img" aria-label="Portrait photograph of the singer against a dark background"></div>

    <div class="personnel">
      <p>Mara Vellin - Voice | Dorian Calloway - Piano</p>
      <p>Clayton Ames - Bass | Miles Ivory - Drums</p>
      <p>Joel Tanner - Trumpet, Flugelhorn, Tenor &amp; Soprano Sax</p>
      <p>Jack Bresson - Percussion | Dan Sorrell - Guitar &amp; Banjo</p>
      <div class="guests">
        <p>* Mick Kenley - hand percussion on Carnival</p>
        <p>* Devon Lark - hand percussion on Carnival</p>
        <p>* Gus Tremaine - piano on Keep the Little One;</p>
        <p>background vocals and hand percussion on Carnival</p>
      </div>
    </div>

    <div class="production">
      <p>Cover art by Ilsa Fenn | Cover design by Ava Claire Tolland</p>
      <p>Produced by Gus Tremaine, SWMA | Recorded at Devon Lark Studios, Cedar Point WA | Mastered by Russ Nordahl, Pine Hollow, WA.</p>
    </div>
  </section>

  <p class="panel-label">BACK (TRAYCARD) FINAL</p>
</div>
</body>
</html>
```